Business Card Design Project : Tidewell Press

In preparation for market launch, Whistler's Tidewell Press require the development of a business card. Tidewell Press is a Community online publishing web portal. We provide the the city of Whistler located in B.C. (Canada) business directories, News, Classified ads, News, Events and blogs etc.

The main focus of the brand is to help local businesses to corporate with their online advertisement and marketing. Meeting our clients face to face is a must (B2B).

Target Market(s)

The target market is B2B customers. Business Owners to Marketing, advertising Managers

Industry/Entity Type

Business

Requirements
Must have
• - The business card will be two sided.
the BACK side will have our logo which consist of (icon, url,slogan) submited. The logo will be middle and centred.

The FRONT side should have company details:

Company Legal Name: FERNDALE TIDEWELL PRESS

Owen Marsk
Director of Sales & Marketing

www.ferndaletidewell.biz
owen@ferndaletidewell.biz

Phone: 555 014 3826
#2817 - 562 E. Harlow Ave.
Vancouver, B.C. K7P2R4 Canada
Nice to have
• - For the "FRONT" side of our business card. You can separate or re-arrange with our logo components (icon, logo,slogan). It does not have to be together.

Also our company legal name is rather long so arrange or organize the name in a way to make it shorter. Your experience and creativity will have to come in play.
Should not have
• should not have other colors beside logo color and black text (2 colors). Also nothing Three dimensional

```html
<!DOCTYPE html>
<html lang="en">
<head>
<meta charset="utf-8">
<title>Ferndale Tidewell Press – Business Card</title>
<link rel="stylesheet" href="https://fonts.googleapis.com/css2?family=Source+Sans+3:ital,wght@0,400;0,600;0,700;1,400&display=swap">
<style>
  :root {
    --backdrop: #080909;
    --card: #ffffff;
    --brand-blue: #2f88f2;
    --ink: #111111;
    --on-blue: #ffffff;
  }
  * { margin: 0; padding: 0; box-sizing: border-box; }
  html, body {
    width: 1200px;
    height: 900px;
    overflow: hidden;
    background: var(--backdrop);
    font-family: "Source Sans 3", "Myriad Pro", Arial, sans-serif;
  }
  .canvas {
    position: relative;
    width: 1200px;
    height: 900px;
  }
  .card {
    position: absolute;
    width: 551px;
    height: 314px;
    background: var(--card);
  }
  .card--front { left: 133px; top: 124px; }
  .card--back { left: 480px; top: 440px; }

  .company-name {
    position: absolute;
    left: 42px;
    top: 74px;
    font-size: 26px;
    font-weight: 700;
    color: var(--brand-blue);
    letter-spacing: 0.2px;
    line-height: 1;
  }
  .name-band {
    position: absolute;
    left: 0;
    top: 106px;
    width: 100%;
    height: 62px;
    background: var(--brand-blue);
    padding: 8px 0 0 42px;
    color: var(--on-blue);
  }
  .person-name {
    font-size: 23px;
    font-weight: 600;
    line-height: 1;
  }
  .person-title {
    font-size: 16px;
    font-style: italic;
    margin-top: 4px;
    line-height: 1;
  }
  .contact-list {
    position: absolute;
    left: 42px;
    top: 172px;
    list-style: none;
    color: var(--brand-blue);
    font-size: 14.5px;
    line-height: 22px;
  }
  .contact-list li { display: flex; align-items: center; }
  .contact-icon {
    width: 16px;
    height: 12px;
    margin-right: 10px;
    flex: none;
  }

  .back-lockup {
    position: absolute;
    left: 0;
    top: 176px;
    width: 100%;
    text-align: center;
  }
  .back-name {
    font-size: 25px;
    font-weight: 700;
    color: var(--ink);
    line-height: 1;
    letter-spacing: -0.2px;
  }
  .back-slogan {
    font-size: 17px;
    color: var(--brand-blue);
    line-height: 1;
    margin-top: 3px;
  }
</style>
</head>
<body>
<main class="canvas">
  <section class="card card--front" aria-label="Card front">
    <h1 class="company-name">FERNDALE TIDEWELL PRESS</h1>
    <div class="name-band">
      <p class="person-name">Owen Marsk</p>
      <p class="person-title">Director of Sales &amp; Marketing</p>
    </div>
    <ul class="contact-list">
      <li>www.ferndaletidewell.biz / owen@ferndaletidewell.biz</li>
      <li>
        <svg class="contact-icon" viewBox="0 0 16 12" aria-hidden="true">
          <path d="M1 4 Q8 -1 15 4 L13 6 L11 4.5 L5 4.5 L3 6 Z" fill="var(--brand-blue)"/>
          <rect x="3" y="6" width="10" height="5.5" rx="1" fill="var(--brand-blue)"/>
          <circle cx="8" cy="8.7" r="1.5" fill="#fff"/>
        </svg>
        555 014 3826
      </li>
      <li>
        <svg class="contact-icon" viewBox="0 0 16 12" aria-hidden="true">
          <rect x="1" y="1" width="14" height="10" fill="none" stroke="var(--brand-blue)" stroke-width="1.6"/>
          <path d="M1 1 L8 7 L15 1 M1 11 L6 5.5 M15 11 L10 5.5" fill="none" stroke="var(--brand-blue)" stroke-width="1.4"/>
        </svg>
        #2817 - 562 E. Harlow Ave. Vancouver, B.C. K7P2R4 Canada
      </li>
    </ul>
  </section>

  <section class="card card--back" aria-label="Card back">
    <div class="back-lockup">
      <p class="back-name">www.ferndaletidewell.biz</p>
      <p class="back-slogan">Your information gateway</p>
    </div>
  </section>
</main>
</body>
</html>
```